Satchel & Compass needs new business card design

I need a new business card design. I'm looking for out-of-the-box design which represents the freedom of being a location independent entrepreneur.
I offer coaching, retreats and trips.
I would like to see designs with and without the photo.
Colors I use are black (#000000), green (#25A796) and brown (#D7C38C)
Website satchelandcompass.com

Target Market(s)

location independent entrepreneurs, digital nomads, people looking to swap the 9 to 5 for a lifestyle business

Industry/Entity Type

Business

Contact Information for Business Card

Petra Varga
Your Lifestyle Business Coach, Retreat & Trip Leader
http://satchelandcompass.com
hello@satchelandcompass.com
Live a life you don't need a holiday from

Font styles to use
Serif
Sans Serif

Requirements
Must have
• One side should contain only the logo. I would also consider having the "Live a life you don't need a holiday from" on that side too (depending on how it looks)
• Please show both sides on the designs.

```html
<!DOCTYPE html>
<html lang="en">
<head>
<meta charset="utf-8">
<title>Satchel &amp; Compass – Business Card</title>
<link href="https://fonts.googleapis.com/css2?family=Montserrat:wght@700&family=Crimson+Text:ital,wght@0,400;1,400&display=swap" rel="stylesheet">
<style>
  :root {
    --black: #000000;
    --green: #25A796;
    --brown: #D7C38C;
    --paper: #ffffff;
    --backdrop: #eeeceb;
  }
  * { box-sizing: border-box; margin: 0; padding: 0; }
  html, body { width: 1200px; height: 676px; overflow: hidden; }
  body {
    background: var(--backdrop);
    position: relative;
    font-family: "Crimson Text", Georgia, serif;
  }
  .card {
    position: absolute;
    top: 195px;
    width: 500px;
    height: 286px;
    background: var(--paper);
    box-shadow: 0 6px 20px rgba(0,0,0,0.12);
    overflow: hidden;
  }
  .card--front { left: 70px; }
  .card--back { left: 630px; }

  /* Front */
  .front-panel {
    position: absolute;
    left: 225px; top: 0; right: 0; bottom: 0;
    background: var(--brown);
    border-left: 4px solid var(--green);
  }
  .contact {
    position: absolute;
    left: 24px; top: 28px;
    width: 190px;
  }
  .contact__name {
    font-family: "Montserrat", Arial, sans-serif;
    font-weight: 700;
    font-size: 21px;
    color: var(--black);
    letter-spacing: 0.2px;
  }
  .contact__role {
    margin-top: 6px;
    font-style: italic;
    font-size: 13px;
    line-height: 1.15;
    color: var(--green);
  }
  .contact__rule {
    margin-top: 8px;
    width: 150px;
    height: 2px;
    background: var(--green);
  }
  .contact__list {
    list-style: none;
    margin-top: 22px;
    font-size: 13px;
    color: var(--green);
  }
  .contact__item {
    display: flex;
    align-items: center;
    gap: 5px;
    line-height: 1.5;
  }
  .contact__item svg { flex: none; }
  .brand {
    font-family: "Montserrat", Arial, sans-serif;
    font-weight: 700;
    color: var(--black);
    text-transform: uppercase;
    letter-spacing: 1px;
    text-align: center;
  }
  .front-panel .brand {
    position: absolute;
    left: 0; right: 0; top: 92px;
    font-size: 22px;
  }
  .tagline {
    position: absolute;
    left: 14px; right: 10px; bottom: 14px;
    font-size: 15px;
    color: var(--black);
  }

  /* Back */
  .edge {
    position: absolute;
    top: 0; bottom: 0;
    width: 22px;
    background: var(--brown);
  }
  .edge--left { left: 0; border-right: 3px solid var(--green); }
  .edge--right { right: 0; border-left: 3px solid var(--green); }
  .card--back .brand {
    position: absolute;
    left: 0; right: 0; top: 124px;
    font-size: 28px;
  }
</style>
</head>
<body>
  <section class="card card--front" aria-label="Business card front">
    <div class="contact">
      <h1 class="contact__name">Petra Varga</h1>
      <p class="contact__role">Your Lifestyle Business Coach,<br>Retreat &amp; Trip Leader</p>
      <div class="contact__rule"></div>
      <ul class="contact__list">
        <li class="contact__item">
          <svg width="13" height="13" viewBox="0 0 13 13" aria-hidden="true">
            <circle cx="6.5" cy="6.5" r="5.5" fill="none" stroke="#25A796" stroke-width="1.3"/>
            <ellipse cx="6.5" cy="6.5" rx="2.4" ry="5.5" fill="none" stroke="#25A796" stroke-width="1"/>
            <line x1="1" y1="6.5" x2="12" y2="6.5" stroke="#25A796" stroke-width="1"/>
          </svg>
          : www.satchelandcompass.com
        </li>
        <li class="contact__item">
          <svg width="15" height="11" viewBox="0 0 15 11" aria-hidden="true">
            <rect x="0.7" y="0.7" width="13.6" height="9.6" fill="none" stroke="#25A796" stroke-width="1.2"/>
            <polyline points="0.7,0.7 7.5,6 14.3,0.7" fill="none" stroke="#25A796" stroke-width="1.2"/>
          </svg>
          : hello@satchelandcompass.com
        </li>
      </ul>
    </div>
    <div class="front-panel">
      <p class="brand">Satchel &amp; Compass</p>
      <p class="tagline">Live a life you don’t need a holiday from</p>
    </div>
  </section>

  <section class="card card--back" aria-label="Business card back">
    <div class="edge edge--left"></div>
    <div class="edge edge--right"></div>
    <p class="brand">Satchel &amp; Compass</p>
  </section>
</body>
</html>
```